Blue Harbor polishing
Project: Business cards and stationary
Business cards and stationary - Automotive
Business cards and stationary
Modern
Ray Mercer
Owner
1735 E. Corbin Rd. Prudenville Mi. 48639
raymercer@mailbrook.net
blueharborshine.us
All logos and lettering is "white" with a black glossy background, I would like to look at tow different logos # 308 and 309. One may look better on the business card. I hope they uploaded!
Visit our website @ blueharborshine.us for a list of services and prices. Visit us on facebook @ Blue Harbor shine

```html
<!DOCTYPE html>
<html lang="en">
<head>
<meta charset="utf-8">
<title>Blue Harbor polishing – Business Cards</title>
<link rel="stylesheet" href="https://fonts.googleapis.com/css2?family=Titillium+Web:wght@300;400;700&display=swap">
<style>
  :root {
    --backdrop: #6b6d6f;
    --card-black: #050505;
    --card-gloss: #262626;
    --ink-white: #ffffff;
    --ink-soft: #c9c9c9;
    --ink-muted: #9a9a9a;
    --corner-mark: #d8d8d8;
  }
  * { margin: 0; padding: 0; box-sizing: border-box; }
  html, body {
    width: 1200px;
    height: 901px;
    overflow: hidden;
    background: var(--backdrop);
    font-family: "Titillium Web", "Helvetica Neue", Arial, sans-serif;
  }
  .stage {
    position: relative;
    width: 1200px;
    height: 901px;
  }
  .card {
    position: absolute;
    left: 280px;
    width: 640px;
    height: 366px;
    background:
      linear-gradient(125deg, transparent 0 55%, rgba(255,255,255,0.07) 55% 70%, transparent 70%),
      radial-gradient(ellipse at 30% 25%, var(--card-gloss) 0%, var(--card-black) 65%);
    border-radius: 6px;
    box-shadow: 0 14px 30px rgba(0,0,0,0.45);
    color: var(--ink-white);
    overflow: hidden;
  }
  .card--front { top: 60px; }
  .card--back { top: 474px; }

  /* Front */
  .brand {
    position: absolute;
    left: 60px;
    top: 112px;
    display: flex;
    align-items: center;
    gap: 14px;
    white-space: nowrap;
  }
  .brand__dot {
    width: 40px;
    height: 40px;
    border-radius: 50%;
    background: var(--ink-white);
    flex: none;
  }
  .brand__name {
    font-weight: 700;
    font-size: 38px;
    line-height: 1;
    text-transform: uppercase;
    letter-spacing: 1px;
    color: var(--ink-white);
  }
  .holder {
    position: absolute;
    left: 62px;
    top: 214px;
    font-weight: 300;
    font-size: 30px;
    color: var(--ink-soft);
    letter-spacing: 0.5px;
    white-space: nowrap;
  }
  .holder__divider { margin: 0 10px; }
  .corner-mark {
    position: absolute;
    bottom: 0;
    width: 26px;
    height: 26px;
    background: var(--corner-mark);
  }
  .corner-mark--left { left: 0; }
  .corner-mark--right { right: 0; }

  /* Back */
  .contact {
    position: absolute;
    right: 60px;
    top: 60px;
    list-style: none;
    font-weight: 400;
    font-size: 19px;
    line-height: 1.75;
    color: var(--ink-white);
    white-space: nowrap;
  }
  .contact__item {
    display: flex;
    align-items: center;
    gap: 10px;
  }
  .contact__icon {
    width: 16px;
    height: 16px;
    flex: none;
    fill: var(--ink-white);
  }
  .contact__address { margin-bottom: 6px; }
  .promo {
    position: absolute;
    left: 60px;
    right: 60px;
    bottom: 48px;
    font-weight: 300;
    font-size: 15px;
    line-height: 1.6;
    color: var(--ink-muted);
  }
  .promo strong { font-weight: 400; color: var(--ink-white); }
</style>
</head>
<body>
<main class="stage">
  <section class="card card--front" aria-label="Business card front">
    <div class="brand">
      <span class="brand__dot" aria-hidden="true"></span>
      <span class="brand__name">Blue Harbor polishing</span>
    </div>
    <p class="holder">Ray Mercer<span class="holder__divider">/</span>Owner</p>
    <span class="corner-mark corner-mark--left" aria-hidden="true"></span>
    <span class="corner-mark corner-mark--right" aria-hidden="true"></span>
  </section>

  <section class="card card--back" aria-label="Business card back">
    <ul class="contact">
      <li class="contact__item contact__address">1735 E. Corbin Rd. Maple Hollow Mi. 48639</li>
      <li class="contact__item">
        <svg class="contact__icon" viewBox="0 0 24 24" aria-hidden="true"><path d="M6.6 10.8a15.1 15.1 0 0 0 6.6 6.6l2.2-2.2a1 1 0 0 1 1-.25 11.4 11.4 0 0 0 3.6.57 1 1 0 0 1 1 1V20a1 1 0 0 1-1 1A17 17 0 0 1 3 4a1 1 0 0 1 1-1h3.5a1 1 0 0 1 1 1c0 1.250.2 2.45.57 3.57a1 1 0 0 1-.25 1z"/></svg>
        (989) 555-0142
      </li>
      <li class="contact__item">
        <svg class="contact__icon" viewBox="0 0 24 24" aria-hidden="true"><path d="M3 5h18a1 1 0 0 1 1 1v12a1 1 0 0 1-1 1H3a1 1 0 0 1-1-1V6a1 1 0 0 1 1-1zm9 7.2L4.5 7v10h15V7z"/></svg>
        raymercer@mailbrook.net
      </li>
      <li class="contact__item">
        <svg class="contact__icon" viewBox="0 0 24 24" aria-hidden="true"><path d="M12 2a10 10 0 1 0 0 20 10 10 0 0 0 0-20zm6.9 9h-3a15.6 15.6 0 0 0-1.3-5.6A8 8 0 0 1 18.9 11zM12 4.1c.9 1.2 1.7 3.6 1.9 6.9h-3.8c.2-3.3 1-5.7 1.9-6.9zM9.4 5.4A15.6 15.6 0 0 0 8.1 11h-3a8 8 0 0 1 4.3-5.6zM5.1 13h3a15.6 15.6 0 0 0 1.3 5.6A8 8 0 0 1 5.1 13zm6.9 6.9c-.9-1.2-1.7-3.6-1.9-6.9h3.8c-.2 3.3-1 5.7-1.9 6.9zm2.6-1.3a15.6 15.6 0 0 0 1.3-5.6h3a8 8 0 0 1-4.3 5.6z"/></svg>
        blueharborshine.us
      </li>
    </ul>
    <p class="promo">
      Visit our website @ <strong>blueharborshine.us</strong> for a list of services and prices.<br>
      Visit us on facebook @ <strong>Blue Harbor shine</strong>
    </p>
  </section>
</main>
</body>
</html>
```